Orvane Yuletide Pageant 2025

We’re looking for a designer to help refresh the visual identity of our annual Christmas show while maintaining continuity from previous years. The updated design should feel festive, and warm, with a sense of celebration and anticipation. We’d like a central graphic that can be adapted for posters, social media, and digital signage, along with supporting assets for flyers and banners.

We’re open to seasonal color palettes such as rich reds, deep greens or blues, golds, silvers, or cool winter tones, and prefer typography that’s clear and elegant. The overall look should feel familiar to returning audiences while inviting and engaging for newcomers.

Two key groups: the current attenders of our congregation and the broader community in our suburb of Rochester, NY. Our congregation is made up of families, older adults, and young professionals who value faith, community and spiritual growth. The surrounding community is a fast growing friendly and family-oriented area of young professionals and longtime families.

We’re looking for a designer to help refresh the visual identity of our annual Christmas show while maintaining continuity with the theme and tone of previous years. The updated design should feel festive, and warm, with a sense of celebration and anticipation. We’d like a central graphic that can be adapted for posters, social media, and digital signage, along with supporting assets for flyers and banners.

Target Market(s)

Two key groups: the current attenders of our congregation and the broader community in our suburb of Rochester, NY. Our congregation is made up of families, older adults, and young professionals who value faith, community and spiritual growth. The surrounding community is a fast growing friendly and family-oriented area of young professionals and long time families.

Industry/Entity Type

Non-profit. Church

Font styles to use
Serif
Decorative
Script
Other font styles liked:
• Quentin

Requirements
Must have
• Sparkle, eye catching
Should not have
• must not look identical to the uploaded versions

```html
<!DOCTYPE html>
<html lang="en">
<head>
<meta charset="utf-8">
<title>Orvane Yuletide Pageant</title>
<link rel="stylesheet" href="https://fonts.googleapis.com/css2?family=Montserrat:ital,wght@0,400;0,500;0,700;1,400&family=Great+Vibes&display=swap">
<style>
  :root {
    --navy-deep: #0b2444;
    --navy: #123f68;
    --teal-light: #6aaecb;
    --ink: #0d1f5c;
    --gold-light: #fff0b8;
    --gold: #e3a632;
    --gold-dark: #9a5a12;
    --spark: rgba(255, 248, 220, 0.95);
    --ice: #7cc4ec;
    --ice-light: #d6f1ff;
    --ribbon: #d9bf8f;
    --pearl: #e8e6e2;
  }
  * { margin: 0; padding: 0; box-sizing: border-box; }
  html, body { width: 1200px; height: 675px; overflow: hidden; background: var(--navy-deep); }
  .poster {
    position: relative;
    width: 1200px;
    height: 675px;
    overflow: hidden;
    font-family: "Montserrat", sans-serif;
  }
  .backdrop {
    position: absolute; inset: 0;
    background:
      radial-gradient(circle 22px at 1150px 78px, rgba(255, 236, 190, 0.95), rgba(255, 236, 190, 0.3) 60%, transparent 75%),
      radial-gradient(circle 16px at 110px 372px, rgba(255, 240, 205, 0.95), rgba(255, 240, 205, 0.25) 60%, transparent 75%),
      radial-gradient(circle 20px at 990px 315px, rgba(230, 240, 245, 0.55), transparent 75%),
      radial-gradient(circle 12px at 1180px 245px, rgba(255, 238, 200, 0.8), transparent 75%),
      radial-gradient(circle 12px at 1120px 224px, rgba(255, 238, 200, 0.7), transparent 75%),
      radial-gradient(circle 10px at 860px 8px, rgba(255, 238, 200, 0.8), transparent 75%),
      radial-gradient(circle 12px at 258px 540px, rgba(255, 230, 180, 0.7), transparent 75%),
      radial-gradient(circle 10px at 850px 485px, rgba(255, 240, 210, 0.8), transparent 75%),
      radial-gradient(circle 14px at 905px 370px, rgba(230, 240, 245, 0.45), transparent 75%),
      radial-gradient(circle 5px at 1065px 150px, var(--spark), transparent 80%),
      radial-gradient(circle 4px at 1010px 190px, var(--spark), transparent 80%),
      radial-gradient(circle 4px at 960px 230px, var(--spark), transparent 80%),
      radial-gradient(circle 4px at 1095px 110px, var(--spark), transparent 80%),
      radial-gradient(circle 3px at 1040px 260px, var(--spark), transparent 80%),
      radial-gradient(circle 3px at 930px 60px, var(--spark), transparent 80%),
      radial-gradient(circle 3px at 1130px 175px, var(--spark), transparent 80%),
      radial-gradient(circle 3px at 985px 120px, var(--spark), transparent 80%),
      radial-gradient(circle 3px at 150px 560px, var(--spark), transparent 80%),
      radial-gradient(circle 3px at 200px 505px, var(--spark), transparent 80%),
      radial-gradient(circle 3px at 560px 40px, var(--spark), transparent 80%),
      radial-gradient(circle 3px at 700px 150px, var(--spark), transparent 80%),
      radial-gradient(circle 3px at 1160px 300px, var(--spark), transparent 80%),
      radial-gradient(ellipse 620px 420px at 70% 8%, rgba(160, 215, 232, 0.75), transparent 70%),
      radial-gradient(ellipse 500px 500px at 0% 55%, rgba(6, 22, 48, 0.85), transparent 70%),
      linear-gradient(135deg, var(--navy-deep) 0%, var(--navy) 45%, var(--teal-light) 100%);
  }
  .ribbon-left {
    position: absolute; left: 0; bottom: 0; width: 470px; height: 140px;
    background: radial-gradient(ellipse 300px 75px at 35% 88%, rgba(217, 191, 143, 0.9), rgba(217, 191, 143, 0.25) 60%, transparent 80%);
  }
  .ornament-cluster {
    position: absolute; right: 0; bottom: 0; width: 380px; height: 400px;
    background:
      radial-gradient(circle 110px at 96% 30%, var(--pearl), rgba(200, 200, 205, 0.5) 60%, transparent 75%),
      radial-gradient(ellipse 240px 170px at 58% 86%, rgba(226, 176, 86, 0.95), rgba(168, 104, 26, 0.5) 60%, transparent 80%);
  }
  .header {
    position: absolute; top: 80px; left: 0; width: 100%;
    text-align: center; color: var(--ink);
  }
  .church-name {
    font-size: 29px; font-weight: 400; letter-spacing: 0.3px; line-height: 1;
  }
  .presents {
    display: flex; align-items: center; justify-content: center; gap: 12px;
    margin-top: 8px; font-size: 28px; font-style: italic; line-height: 1;
  }
  .presents .rule { width: 155px; height: 2px; background: var(--ink); }
  .glitter-gold {
    background:
      radial-gradient(circle at 20% 30%, var(--spark) 0 1.2px, transparent 2px) 0 0 / 9px 11px,
      radial-gradient(circle at 70% 60%, var(--gold-light) 0 1px, transparent 1.8px) 0 0 / 7px 8px,
      radial-gradient(circle at 50% 50%, rgba(120, 60, 0, 0.55) 0 1px, transparent 1.6px) 2px 3px / 6px 7px,
      linear-gradient(180deg, var(--gold-light) 0%, var(--gold) 40%, var(--gold-dark) 70%, var(--gold) 88%, var(--gold-light) 100%);
    -webkit-background-clip: text; background-clip: text;
    color: transparent;
    filter: drop-shadow(0 0 6px rgba(255, 210, 120, 0.45));
  }
  .title-line {
    position: absolute; left: 0; width: 100%; text-align: center;
    font-size: 78px; font-weight: 500; letter-spacing: 20px; line-height: 1;
    padding-left: 20px;
  }
  .title-line.first { top: 182px; }
  .title-line.second { top: 258px; }
  .title-script {
    position: absolute; top: 334px; left: 0; width: 100%; text-align: center;
    font-family: "Great Vibes", cursive; font-size: 156px; line-height: 1;
  }
  .title-underline {
    position: absolute; top: 484px; left: 347px; width: 558px; height: 3px;
    background: linear-gradient(90deg, transparent, var(--gold) 10%, var(--gold-light) 50%, var(--gold) 90%, transparent);
    box-shadow: 0 0 6px rgba(255, 215, 130, 0.6);
  }
  .dates {
    position: absolute; top: 538px; left: 0; width: 100%; text-align: center;
    font-size: 33px; font-weight: 700; letter-spacing: 5px; line-height: 1;
    background:
      radial-gradient(circle at 30% 40%, rgba(255, 255, 255, 0.9) 0 1px, transparent 1.8px) 0 0 / 8px 9px,
      linear-gradient(180deg, var(--ice-light), var(--ice) 60%, #4e9fd6);
    -webkit-background-clip: text; background-clip: text; color: transparent;
  }
</style>
</head>
<body>
<main class="poster">
  <div class="backdrop" role="img" aria-label="Deep blue winter background with sparkling bokeh lights"></div>
  <div class="ribbon-left" role="img" aria-label="Flowing champagne satin ribbon"></div>
  <div class="ornament-cluster" role="img" aria-label="Pearl Christmas bauble with gold glitter leaves and ribbon"></div>

  <header class="header">
    <p class="church-name">HARBORLIGHT COMMUNITY CHURCH</p>
    <p class="presents"><span class="rule"></span>Presents<span class="rule"></span></p>
  </header>

  <h1>
    <span class="title-line first glitter-gold">ORVANE</span>
    <span class="title-line second glitter-gold">YULETIDE</span>
    <span class="title-script glitter-gold">Pageant</span>
  </h1>
  <div class="title-underline"></div>

  <p class="dates">DECEMBER 16 &amp; 17 _ 6:00 PM</p>
</main>
</body>
</html>
```